Mobile App UI for Telecommunications/Hosting Company

We are about to convert our existing self-service Customer Portal into a mobile phone application and need an elegant and professional UI/UX design. Our company provides telecommunication (voice/mobile/data) and hosting services to medium-sized business. The primary purpose of the application is to view trouble tickets, alerts, orders, and performance charts. This application is available to customers only - not the general public.

Please provide a UI design suitable for display on iPhone/Android devices. The attached document includes a proposed screen flow. You are free to design your own screens to display the same information elegantly.
Updates

Please note that the design should be based on the wireframes in the Word document, not the screenshots.  The screenshots are just to show our existing web portal look & feel.

Also, just a few screens are required for initial submission (3 would be great).

Thanks,
Dermot.

Target Market(s)

IT Managers away from their desk and using a mobile phone application.
Adult males from technical background aged 30-50.
Customers of Brindlewood Networks have access to this application (not the general public). This is a self-service portal for customers only.

Industry/Entity Type

Business

Colors
0592cd
33a6d7
85cae6
cadf82
fde08a

Requirements
Must have
• Please look at the screenshots from our current Customer Portal site (part of the project brief). The mobile app does not have to look the same, but should follow a similar style.

Please check out our company web site at www.brindlewoodnetworks.example (this site is not the customer portal and has a different look at feel) to understand what Brindlewood Networks does.
Nice to have
• Sharing capabilities via email/SMS.
A nice background image to make it stand out
The colours selected below are a guide only as they are similar to the corporate colours
- The priority is something that works on a phone - a design extendable to tablets is a nice to have as our existing web site looks OK on a tablet..

```html
<!DOCTYPE html>
<html lang="en">
<head>
<meta charset="UTF-8">
<title>Brindlewood Networks – Sign in</title>
<link rel="stylesheet" href="https://fonts.googleapis.com/css2?family=Open+Sans:wght@400;600;700&display=swap">
<style>
  :root {
    --bg-dark: #3f3f3d;
    --bg-mid: #6b6a66;
    --bg-light: #b9b8b2;
    --accent-yellow: #fde08a;
    --button-text: #1f3f8f;
    --text-light: #ffffff;
    --text-soft: rgba(255, 255, 255, 0.88);
    --field-border: rgba(255, 255, 255, 0.7);
    --field-fill: rgba(255, 255, 255, 0.06);
  }
  * { box-sizing: border-box; margin: 0; padding: 0; }
  html, body {
    width: 677px;
    height: 1200px;
    overflow: hidden;
    background: var(--bg-dark);
    font-family: "Open Sans", "Segoe UI", sans-serif;
  }
  .screen {
    position: relative;
    width: 677px;
    height: 1200px;
    overflow: hidden;
  }
  .backdrop {
    position: absolute;
    inset: 0;
    background:
      radial-gradient(ellipse 260px 420px at 640px 640px, rgba(235,232,222,0.75), rgba(235,232,222,0) 70%),
      radial-gradient(ellipse 200px 300px at 560px 300px, rgba(160,158,150,0.5), rgba(160,158,150,0) 70%),
      radial-gradient(ellipse 260px 260px at 120px 1000px, rgba(120,110,95,0.45), rgba(120,110,95,0) 70%),
      linear-gradient(100deg, var(--bg-dark) 0%, #555450 45%, var(--bg-mid) 70%, var(--bg-light) 100%);
  }
  .brand-name {
    position: absolute;
    left: 79px;
    top: 196px;
    width: 520px;
    color: var(--text-light);
    font-size: 42px;
    font-weight: 400;
    line-height: 56px;
    white-space: nowrap;
  }
  .headline {
    position: absolute;
    top: 388px;
    width: 100%;
    text-align: center;
    color: var(--text-light);
    font-size: 36px;
    font-weight: 600;
  }
  .field {
    position: absolute;
    left: 77px;
    width: 523px;
    height: 100px;
    border: 2px solid var(--field-border);
    background: var(--field-fill);
    display: flex;
    align-items: center;
    padding-left: 24px;
    gap: 22px;
    color: var(--text-soft);
    font-size: 32px;
    white-space: nowrap;
  }
  .field-email { top: 501px; }
  .field-password { top: 634px; }
  .field-icon { width: 54px; height: 54px; flex: none; }
  .remember {
    position: absolute;
    left: 81px;
    top: 790px;
    display: flex;
    align-items: center;
    gap: 24px;
    color: var(--text-light);
    font-size: 30px;
    font-weight: 600;
  }
  .checkbox {
    width: 26px;
    height: 26px;
    border: 2px solid var(--field-border);
  }
  .sign-in {
    position: absolute;
    left: 77px;
    top: 889px;
    width: 523px;
    height: 104px;
    background: var(--accent-yellow);
    color: var(--button-text);
    font-size: 34px;
    font-weight: 600;
    letter-spacing: 1px;
    display: flex;
    align-items: center;
    justify-content: center;
  }
  .forgot {
    position: absolute;
    top: 1046px;
    width: 100%;
    text-align: center;
    color: var(--text-soft);
    font-size: 30px;
  }
</style>
</head>
<body>
<main class="screen">
  <div class="backdrop" role="img" aria-label="Soft blurred office photograph in warm greys behind the sign-in form"></div>

  <p class="brand-name">Brindlewood Networks</p>

  <h1 class="headline">Sign in to your account</h1>

  <div class="field field-email">
    <svg class="field-icon" viewBox="0 0 54 54" aria-hidden="true">
      <rect x="6" y="13" width="42" height="28" rx="3" fill="none" stroke="#fde08a" stroke-width="3.5"/>
      <path d="M7 15 L27 30 L47 15" fill="none" stroke="#fde08a" stroke-width="3.5" stroke-linejoin="round"/>
    </svg>
    <span>yourname@example.com</span>
  </div>

  <div class="field field-password">
    <svg class="field-icon" viewBox="0 0 54 54" aria-hidden="true">
      <path d="M17 24 V17 a10 10 0 0 1 20 0 V24" fill="none" stroke="#fde08a" stroke-width="3.5"/>
      <rect x="11" y="24" width="32" height="24" rx="3" fill="none" stroke="#fde08a" stroke-width="3.5"/>
      <circle cx="27" cy="34" r="3" fill="#fde08a"/>
      <rect x="25.5" y="35" width="3" height="7" fill="#fde08a"/>
    </svg>
    <span>Password</span>
  </div>

  <div class="remember">
    <span class="checkbox"></span>
    <span>Remember me</span>
  </div>

  <div class="sign-in">SIGN IN</div>

  <p class="forgot">Forgot Password?</p>
</main>
</body>
</html>
```